Infographic Business Process Flowchart

Hi there, I need an infographic designed of one of our company process. We have had someone design something already but we weren't happy with it. Could you please let me know if you could design this? The information we need designed is in the PDF attachment "VelmoPath - One Page". The rest are examples of other flowchart infographics we like. Thanks!

Target Market(s)

Internal company

Industry/Entity Type

Tech

Font styles to use
Sans Serif

Colors

Designer to choose colors to be used in the design.

Requirements
Must have
• Information from "VelmoPath - One Page" document
• Style like one of the samples sent
Nice to have
• Company colours which can be found at velmorix.example

```html
<!DOCTYPE html>
<html lang="en">
<head>
<meta charset="utf-8">
<title>Infographic Business Process Flowchart</title>
<link href="https://fonts.googleapis.com/css2?family=Montserrat:wght@400;500;700;800&display=swap" rel="stylesheet">
<style>
:root{
  --navy:#14137a;
  --deep:#0c2461;
  --blue:#1d72c6;
  --yellow:#f8cf48;
  --green:#7cc652;
  --pink:#e26f9b;
  --violet:#9a73cb;
  --ink:#1d1d2b;
  --body:#2f2f3a;
  --orange:#f6a25a;
  --purple:#772f9b;
  --red:#c8141e;
  --tint-blue:#dce9f8;
  --tint-yellow:#fdf0c4;
  --tint-green:#e4f4d9;
  --tint-navy:#dde2ef;
}
*{margin:0;padding:0;box-sizing:border-box}
html,body{width:1200px;height:2778px;overflow:hidden;background:#fff}
body{font-family:"Montserrat",sans-serif;color:var(--body);position:relative}
.board{position:absolute;left:0;top:0;width:1100px;height:2546px;overflow:hidden;transform:scale(1.0909);transform-origin:0 0}
.header{position:absolute;left:0;top:0;width:748px;height:199px;background:var(--navy);color:#f2f2f6;text-align:center;padding-top:36px}
.header h1{font-weight:800;font-size:57px;line-height:66px;letter-spacing:.2px}
.legend{position:absolute;left:855px;top:22px}
.legend-item{display:flex;align-items:center;height:56px;font-weight:700;font-size:15px;color:var(--ink)}
.legend-item svg{width:50px;height:42px;margin-right:32px}
.flow{position:absolute;left:0;top:0;width:1100px;height:2546px}
.art{position:absolute;width:92px;height:88px;border-radius:14px}
.art.b{background:var(--tint-blue)}
.art.y{background:var(--tint-yellow)}
.art.g{background:var(--tint-green)}
.art.n{background:var(--tint-navy)}
.step{position:absolute;width:250px}
.step-head{display:flex;align-items:center;min-height:28px}
.num{width:28px;height:28px;border-radius:50%;color:#fff;font-weight:700;font-size:15px;display:grid;place-items:center;flex:none;margin-right:12px}
.num.b{background:var(--blue)}.num.y{background:var(--yellow)}.num.g{background:var(--green)}.num.n{background:var(--deep)}
.title{font-weight:700;font-size:16px;line-height:16px;color:var(--ink)}
.rows{margin-top:14px}
.row{display:flex;align-items:flex-start;margin-bottom:13px}
.ico{width:40px;flex:none;display:flex;justify-content:center;margin-left:-6px;margin-right:6px}
.ico svg{width:28px;height:26px}
.txt{font-size:11px;line-height:15px;letter-spacing:-.1px;color:var(--body);white-space:nowrap}
.celebrate{position:absolute;left:902px;top:1508px;width:173px;height:57px;background:var(--deep);color:#fff;font-weight:700;font-size:15px;line-height:16px;padding:11px 0 0 20px}
.band{position:absolute;left:0;width:745px;color:#fff;font-weight:700;font-size:14.5px;display:grid;place-items:center}
.band.time{top:2385px;height:46px;background:var(--orange)}
.band.collab{top:2443px;height:47px;background:var(--purple)}
.band.govern{top:2500px;height:44px;background:var(--red)}
.notes{position:absolute;left:758px;top:2384px;width:338px;font-size:9.2px;line-height:13.3px;letter-spacing:-.15px;color:var(--ink);white-space:nowrap;overflow:hidden}
</style>
</head>
<body>
<svg width="0" height="0" style="position:absolute" aria-hidden="true">
  <defs>
    <symbol id="i-team" viewBox="0 0 28 26">
      <g fill="none" stroke="var(--pink)" stroke-width="1.4">
        <circle cx="8" cy="7" r="3.2"/><circle cx="20" cy="7" r="3.2"/><circle cx="14" cy="11" r="3.4"/>
        <path d="M2 17c0-3 3-5 6-5M26 17c0-3-3-5-6-5M7 24c0-4 3-7 7-7s7 3 7 7z"/>
      </g>
    </symbol>
    <symbol id="i-activity" viewBox="0 0 28 26">
      <g fill="none" stroke="var(--pink)" stroke-width="1.4">
        <rect x="2" y="3" width="24" height="20" rx="2"/>
        <path d="M2 8h24M6 12h5M6 15h10M6 18h16"/>
      </g>
    </symbol>
    <symbol id="i-system" viewBox="0 0 28 26">
      <g fill="none" stroke="var(--violet)" stroke-width="1.4">
        <circle cx="10" cy="15" r="6" stroke-dasharray="3 1.6"/><circle cx="10" cy="15" r="2.4"/>
        <circle cx="20" cy="7" r="4.5" stroke-dasharray="2.4 1.4"/><circle cx="20" cy="7" r="1.6"/>
        <circle cx="21" cy="20" r="3.5" stroke-dasharray="2 1.2"/>
      </g>
    </symbol>
    <path id="ah" d="M-13,-5H0V-11L13,0L0,11V5H-13Z"/>
  </defs>
</svg>

<main class="board">
  <header class="header"><h1>Infographic Business<br>Process Flowchart</h1></header>

  <div class="legend">
    <div class="legend-item"><svg><use href="#i-team"/></svg>Team</div>
    <div class="legend-item"><svg><use href="#i-activity"/></svg>Activity</div>
    <div class="legend-item"><svg><use href="#i-system"/></svg>System</div>
  </div>

  <svg class="flow" viewBox="0 0 1100 2546" aria-hidden="true">
    <g fill="none" stroke-width="2" stroke-linecap="round" stroke-dasharray="0.1 5">
      <g stroke="var(--blue)">
        <path d="M220 301H350M487 301H620M755 301H890"/>
      </g>
      <path stroke="var(--yellow)" d="M1025 303H1067V757H1005"/>
      <g stroke="var(--green)">
        <path d="M760 757H890M497 757H625M230 757H360"/>
        <path d="M120 757H67V1215H95"/>
        <path d="M230 1215H355M493 1215H620M765 1215H900"/>
        <path d="M1040 1215H1067V1508"/>
      </g>
      <g stroke="var(--deep)">
        <path d="M1066 1565V1680H1030"/>
        <path d="M760 1680H890M515 1680H630M233 1680H378"/>
        <path d="M110 1680H55V2040H100"/>
        <path d="M240 2040H370M508 2040H633M770 2040H880"/>
      </g>
    </g>
    <g fill="var(--blue)">
      <use href="#ah" transform="translate(285 301)"/><use href="#ah" transform="translate(553 301)"/><use href="#ah" transform="translate(823 301)"/>
    </g>
    <use href="#ah" fill="var(--yellow)" transform="translate(1067 512) rotate(90)"/>
    <g fill="var(--green)">
      <use href="#ah" transform="translate(823 757) rotate(180)"/><use href="#ah" transform="translate(553 757) rotate(180)"/><use href="#ah" transform="translate(290 757) rotate(180)"/>
      <use href="#ah" transform="translate(67 985) rotate(90)"/>
      <use href="#ah" transform="translate(287 1215)"/><use href="#ah" transform="translate(553 1215)"/><use href="#ah" transform="translate(830 1215)"/>
      <use href="#ah" transform="translate(1067 1355) rotate(90)"/>
    </g>
    <g fill="var(--deep)">
      <use href="#ah" transform="translate(1066 1620) rotate(90)"/>
      <use href="#ah" transform="translate(828 1680) rotate(180)"/><use href="#ah" transform="translate(573 1680) rotate(180)"/><use href="#ah" transform="translate(300 1680) rotate(180)"/>
      <use href="#ah" transform="translate(55 1875) rotate(90)"/>
      <use href="#ah" transform="translate(305 2040)"/><use href="#ah" transform="translate(570 2040)"/><use href="#ah" transform="translate(825 2040)"/>
    </g>
  </svg>

  <div class="art b" style="left:102px;top:256px" role="img" aria-label="Line icon of a business person with arrows pointing outward"></div>
  <div class="art b" style="left:379px;top:261px" role="img" aria-label="Line icon of stacked documents with a dollar sign"></div>
  <div class="art b" style="left:639px;top:256px" role="img" aria-label="Line icon of a document template"></div>
  <div class="art y" style="left:911px;top:256px" role="img" aria-label="Line icon of an envelope with an at sign"></div>

  <div class="art g" style="left:117px;top:713px" role="img" aria-label="Line icon of a strategy plan scroll"></div>
  <div class="art g" style="left:386px;top:713px" role="img" aria-label="Line icon of a calendar with a check mark"></div>
  <div class="art g" style="left:649px;top:713px" role="img" aria-label="Line icon of a group of people"></div>
  <div class="art g" style="left:911px;top:713px" role="img" aria-label="Line icon of a person with a gear"></div>

  <div class="art g" style="left:117px;top:1171px" role="img" aria-label="Line icon of a strategy plan scroll"></div>
  <div class="art g" style="left:379px;top:1171px" role="img" aria-label="Line icon of gears"></div>
  <div class="art g" style="left:649px;top:1171px" role="img" aria-label="Line icon of a circle with a minus sign"></div>
  <div class="art g" style="left:921px;top:1176px" role="img" aria-label="Line icon of a stack of books"></div>

  <div class="art n" style="left:117px;top:1646px" role="img" aria-label="Line icon of a gear with circular arrows"></div>
  <div class="art n" style="left:399px;top:1646px" role="img" aria-label="Line icon of a rising bar chart"></div>
  <div class="art n" style="left:657px;top:1656px" role="img" aria-label="Line icon of satisfaction feedback bubbles"></div>
  <div class="art n" style="left:914px;top:1651px" role="img" aria-label="Line icon of a support agent with headset"></div>

  <div class="art n" style="left:132px;top:1996px" role="img" aria-label="Line icon of a document with a magnifying glass"></div>
  <div class="art n" style="left:382px;top:1996px" role="img" aria-label="Line icon of a support agent with headset"></div>
  <div class="art n" style="left:654px;top:1991px" role="img" aria-label="Line icon of a person inside a gear"></div>
  <div class="art n" style="left:902px;top:1996px" role="img" aria-label="Large outline lettering of a currency symbol"></div>

  <section class="step" style="left:79px;top:369px">
    <div class="step-head"><span class="num b">1</span><h2 class="title">Create<br>Opportunity</h2></div>
    <div class="rows">
      <div class="row"><span class="ico"><svg><use href="#i-team"/></svg></span><p class="txt">Sales</p></div>
      <div class="row"><span class="ico"><svg><use href="#i-activity"/></svg></span><p class="txt">Sales Team Creates<br>an Opportunity in<br>LinkDesk</p></div>
      <div class="row"><span class="ico"><svg><use href="#i-system"/></svg></span><p class="txt">LinkDesk</p></div>
    </div>
  </section>
  <section class="step" style="left:342px;top:372px">
    <div class="step-head"><span class="num b">2</span><h2 class="title">Convert to<br>Sales Order</h2></div>
    <div class="rows">
      <div class="row"><span class="ico"><svg><use href="#i-team"/></svg></span><p class="txt">Sales</p></div>
      <div class="row"><span class="ico"><svg><use href="#i-activity"/></svg></span><p class="txt">Operation converts<br>won opportunities are<br>converts it to a Sales<br>Order</p></div>
      <div class="row"><span class="ico"><svg><use href="#i-system"/></svg></span><p class="txt">LinkDesk</p></div>
    </div>
  </section>
  <section class="step" style="left:607px;top:373px">
    <div class="step-head"><span class="num b">3</span><h2 class="title">Create Project<br>Template</h2></div>
    <div class="rows">
      <div class="row"><span class="ico"><svg><use href="#i-team"/></svg></span><p class="txt">Operations</p></div>
      <div class="row"><span class="ico"><svg><use href="#i-activity"/></svg></span><p class="txt">Operation converts the<br>Sales order to a Project<br>in LinkDesk</p></div>
      <div class="row"><span class="ico"><svg><use href="#i-system"/></svg></span><p class="txt">LinkDesk</p></div>
    </div>
  </section>
  <section class="step" style="left:868px;top:372px">
    <div class="step-head"><span class="num y">4</span><h2 class="title">Contact Client</h2></div>
    <div class="rows">
      <div class="row"><span class="ico"><svg><use href="#i-team"/></svg></span><p class="txt">Services</p></div>
      <div class="row"><span class="ico"><svg><use href="#i-activity"/></svg></span><p class="txt">Services contact client<br>to acknowledge<br>opportunity and advise<br>of process (This could<br>be automated by<br>Operations / For bigger<br>projects Sale can<br>contact them) - Sales<br>provides contact name,<br>project high level<br>summary</p></div>
      <div class="row"><span class="ico"><svg><use href="#i-system"/></svg></span><p class="txt">Email or In person for<br>&gt; 100K projects</p></div>
    </div>
  </section>

  <section class="step" style="left:875px;top:817px">
    <div class="step-head"><span class="num g">5</span><h2 class="title">Assign PM</h2></div>
    <div class="rows">
      <div class="row"><span class="ico"><svg><use href="#i-team"/></svg></span><p class="txt">Services - PMO</p></div>
      <div class="row"><span class="ico"><svg><use href="#i-activity"/></svg></span><p class="txt">Services assign project<br>manager</p></div>
      <div class="row"><span class="ico"><svg><use href="#i-system"/></svg></span><p class="txt">Project Manager<br>Capacity Sheet</p></div>
    </div>
  </section>
  <section class="step" style="left:615px;top:818px">
    <div class="step-head"><span class="num g">6</span><h2 class="title">Create Team<br>Site</h2></div>
    <div class="rows">
      <div class="row"><span class="ico"><svg><use href="#i-team"/></svg></span><p class="txt">Services - PMO</p></div>
      <div class="row"><span class="ico"><svg><use href="#i-activity"/></svg></span><p class="txt">Services creates Team<br>channel for Project<br>under client site Project<br>channel contains<br>templates for project<br>management and<br>checklist for different<br>phases of the<br>engagement</p></div>
      <div class="row"><span class="ico"><svg><use href="#i-system"/></svg></span><p class="txt">TeamHub</p></div>
    </div>
  </section>
  <section class="step" style="left:348px;top:814px">
    <div class="step-head"><span class="num g">7</span><h2 class="title">Initiation</h2></div>
    <div class="rows">
      <div class="row"><span class="ico"><svg><use href="#i-team"/></svg></span><p class="txt">Services – PMO<br>&amp; Project Team</p></div>
      <div class="row"><span class="ico"><svg><use href="#i-activity"/></svg></span><p class="txt">- Project Manager and<br>&nbsp;&nbsp;Sales Handover<br>- Project Manager and<br>&nbsp;&nbsp;Practice define team<br>- Internal Kick off<br>- Pre Client Kick off<br>- Client Kick off</p></div>
      <div class="row"><span class="ico"><svg><use href="#i-system"/></svg></span><p class="txt">PlanMaster, TeamHub,<br>LinkDesk</p></div>
    </div>
  </section>
  <section class="step" style="left:85px;top:814px">
    <div class="step-head"><span class="num g">8</span><h2 class="title">Planning</h2></div>
    <div class="rows">
      <div class="row"><span class="ico"><svg><use href="#i-team"/></svg></span><p class="txt">Services – PMO<br>&amp; Project Team</p></div>
      <div class="row"><span class="ico"><svg><use href="#i-activity"/></svg></span><p class="txt">- Gather Requirements<br>- Create WBS<br>- Schedule Resources<br>- Highlight RAID<br>- Refine SoW<br>- Refine Project Plan<br>- Commitment and<br>&nbsp;&nbsp;Acceptance of<br>&nbsp;&nbsp;Requirem</p></div>
      <div class="row"><span class="ico"><svg><use href="#i-system"/></svg></span><p class="txt">PlanMaster, Workshop<br>Templates in TeamHub, User<br>Stories in Trakka / Cobalt<br>Ops, LinkDesk</p></div>
    </div>
  </section>

  <section class="step" style="left:81px;top:1269px">
    <div class="step-head"><span class="num g">8</span><h2 class="title">Planning</h2></div>
    <div class="rows">
      <div class="row"><span class="ico"><svg><use href="#i-team"/></svg></span><p class="txt">Services – PMO<br>&amp; Project Team</p></div>
      <div class="row"><span class="ico"><svg><use href="#i-activity"/></svg></span><p class="txt">- Gather Requirements<br>- Create WBS<br>- Schedule Resources<br>- Highlight RAID<br>- Refine SoW<br>- Refine Project Plan<br>- Commitment and<br>&nbsp;&nbsp;Acceptance of<br>&nbsp;&nbsp;Requirem</p></div>
      <div class="row"><span class="ico"><svg><use href="#i-system"/></svg></span><p class="txt">PlanMaster, Workshop<br>Templates in TeamHub, User<br>Stories in Trakka / Cobalt<br>Ops, LinkDesk</p></div>
    </div>
  </section>
  <section class="step" style="left:348px;top:1270px">
    <div class="step-head"><span class="num g">9</span><h2 class="title">Initiation</h2></div>
    <div class="rows">
      <div class="row"><span class="ico"><svg><use href="#i-team"/></svg></span><p class="txt">Services – PMO<br>&amp; Project Team</p></div>
      <div class="row"><span class="ico"><svg><use href="#i-activity"/></svg></span><p class="txt">Build the various<br>aspects of a solution in<br>accordance with Plan<br>Track deliverables,<br>such as designs, plans,<br>schedules, and<br>requirements and<br>maintain:<br>- Release Notes<br>- Test Results<br>- Source Code<br>- Project<br>&nbsp;&nbsp;Documentation</p></div>
      <div class="row"><span class="ico"><svg><use href="#i-system"/></svg></span><p class="txt">PlanMaster, Cobalt Ops /<br>Trakka, LinkDesk</p></div>
    </div>
  </section>
  <section class="step" style="left:615px;top:1270px">
    <div class="step-head"><span class="num g">10</span><h2 class="title">Closure</h2></div>
    <div class="rows">
      <div class="row"><span class="ico"><svg><use href="#i-team"/></svg></span><p class="txt">Services – PMO<br>&amp; Project Team</p></div>
      <div class="row"><span class="ico"><svg><use href="#i-activity"/></svg></span><p class="txt">- Customer Acceptance<br>- Project Close out &amp;<br>&nbsp;&nbsp;Support Planning<br>&nbsp;&nbsp;Performance Review<br>- Lessons Learnt<br>- IP Session</p></div>
      <div class="row"><span class="ico"><svg><use href="#i-system"/></svg></span><p class="txt">PlanMaster, TeamHub,<br>LinkDesk</p></div>
    </div>
  </section>
  <section class="step" style="left:875px;top:1270px">
    <div class="step-head"><span class="num g">11</span><h2 class="title">Lessons Learnt</h2></div>
    <div class="rows">
      <div class="row"><span class="ico"><svg><use href="#i-team"/></svg></span><p class="txt">Services – PMO &amp;<br>Practice</p></div>
      <div class="row"><span class="ico"><svg><use href="#i-activity"/></svg></span><p class="txt">What Went Well &amp; What<br>Didn't IP?</p></div>
      <div class="row"><span class="ico"><svg><use href="#i-system"/></svg></span><p class="txt">TeamHub at Project<br>Level, DocSpace at<br>Offering / Solution Level</p></div>
    </div>
  </section>

  <div class="celebrate">Celebrate<br>Success</div>

  <section class="step" style="left:882px;top:1758px">
    <div class="step-head"><span class="num n">12</span><h2 class="title">Support</h2></div>
    <div class="rows">
      <div class="row"><span class="ico"><svg><use href="#i-team"/></svg></span><p class="txt">Services / Managed<br>Services</p></div>
      <div class="row"><span class="ico"><svg><use href="#i-activity"/></svg></span><p class="txt">TBD</p></div>
      <div class="row"><span class="ico"><svg><use href="#i-system"/></svg></span><p class="txt">Support Tickets in<br>LinkDesk</p></div>
    </div>
  </section>
  <section class="step" style="left:622px;top:1757px">
    <div class="step-head"><span class="num n">13</span><h2 class="title">Customer<br>Satisfaction</h2></div>
    <div class="rows">
      <div class="row"><span class="ico"><svg><use href="#i-team"/></svg></span><p class="txt">Operations \ Sales</p></div>
      <div class="row"><span class="ico"><svg><use href="#i-activity"/></svg></span><p class="txt">Operations &nbsp;sends<br>Customer Satisfaction<br>survey</p></div>
      <div class="row"><span class="ico"><svg><use href="#i-system"/></svg></span><p class="txt">Forms</p></div>
    </div>
  </section>
  <section class="step" style="left:354px;top:1754px">
    <div class="step-head"><span class="num n">14</span><h2 class="title">Project Based<br>Performance</h2></div>
    <div class="rows">
      <div class="row"><span class="ico"><svg><use href="#i-team"/></svg></span><p class="txt">Operations \ Sales</p></div>
      <div class="row"><span class="ico"><svg><use href="#i-activity"/></svg></span><p class="txt">Operations &nbsp;sends<br>Customer Satisfaction<br>survey</p></div>
      <div class="row"><span class="ico"><svg><use href="#i-system"/></svg></span><p class="txt">Forms</p></div>
    </div>
  </section>
  <section class="step" style="left:87px;top:1751px">
    <div class="step-head"><span class="num n">15</span><h2 class="title">Operations</h2></div>
    <div class="rows">
      <div class="row"><span class="ico"><svg><use href="#i-team"/></svg></span><p class="txt">Operations</p></div>
      <div class="row"><span class="ico"><svg><use href="#i-activity"/></svg></span><p class="txt">Operations conducts<br>review on project with<br>practice and PMO team</p></div>
      <div class="row"><span class="ico"><svg><use href="#i-system"/></svg></span><p class="txt">Forms</p></div>
    </div>
  </section>

  <section class="step" style="left:87px;top:2096px">
    <div class="step-head"><span class="num n">16</span><h2 class="title">Case Study</h2></div>
    <div class="rows">
      <div class="row"><span class="ico"><svg><use href="#i-team"/></svg></span><p class="txt">Marketing</p></div>
      <div class="row"><span class="ico"><svg><use href="#i-activity"/></svg></span><p class="txt">Marketing Compiles a<br>Case Study on the<br>project</p></div>
    </div>
  </section>
  <section class="step" style="left:351px;top:2097px">
    <div class="step-head"><span class="num n">17</span><h2 class="title">Support</h2></div>
    <div class="rows">
      <div class="row"><span class="ico"><svg><use href="#i-team"/></svg></span><p class="txt">Services / Managed<br>Services</p></div>
      <div class="row"><span class="ico"><svg><use href="#i-activity"/></svg></span><p class="txt">Ensure support<br>continues in a seamless<br>fashion from one<br>agreement to the next<br>Monthly Report<br>showing the calls<br>managed during the<br>period and including<br>those opened and<br>closed over the period</p></div>
      <div class="row"><span class="ico"><svg><use href="#i-system"/></svg></span><p class="txt">LinkDesk</p></div>
    </div>
  </section>
  <section class="step" style="left:622px;top:2091px">
    <div class="step-head"><span class="num n">18</span><h2 class="title">Human<br>Resources</h2></div>
    <div class="rows">
      <div class="row"><span class="ico"><svg><use href="#i-team"/></svg></span><p class="txt">Operations</p></div>
      <div class="row"><span class="ico"><svg><use href="#i-activity"/></svg></span><p class="txt">Recruitment<br>Staff Assessments and<br>Training WH&amp;S<br>Payroll including<br>Reimbursements</p></div>
      <div class="row"><span class="ico"><svg><use href="#i-system"/></svg></span><p class="txt">LinkDesk,<br>Birch HR, Ledgerly</p></div>
    </div>
  </section>
  <section class="step" style="left:884px;top:2094px">
    <div class="step-head"><span class="num n">19</span><h2 class="title">Finance/<br>ODS</h2></div>
    <div class="rows">
      <div class="row"><span class="ico"><svg><use href="#i-team"/></svg></span><p class="txt">Operations</p></div>
      <div class="row"><span class="ico"><svg><use href="#i-activity"/></svg></span><p class="txt">- Invoicing<br>- Purchasing<br>- Financial Report</p></div>
      <div class="row"><span class="ico"><svg><use href="#i-system"/></svg></span><p class="txt">LinkDesk,<br>Ledgerly</p></div>
    </div>
  </section>

  <div class="band time">Time Sheets in LinkDesk</div>
  <div class="band collab">Project Collaboration in TeamHub</div>
  <div class="band govern">Control and Governance</div>

  <div class="notes">
    Team<br>Services<br>Action:<br>
    Stakeholder management through routine project status meeting<br>
    Provide Budget update to client<br>
    Routine meeting with Team to highlight risks and mitigation plans<br>
    Identify opportunities<br>
    Apply technical governance process<br>
    Systems<br>LinkDesk<br>PlanMaster<br>TeamHub
  </div>
</main>
</body>
</html>
```